依頼詳細
<取扱商品>
レディースバレエシューズ・ルームシューズ・除菌スプレー・マスクケースなど

<ターゲット>
やや女性向け
基本は老若男女問わず

<使用画像について>
商品画像はコンペ終了後にお渡ししますので仮の画像を入れていただければと思います。
商品画像以外の使用素材は有料のものでも問題は有りませんが、quilva picsまたは低価格(0~2000円程度)のものでお願いします。
※もし有料素材を使う場合は最初から購入して頂く必要はないのでウォーターマーク付きのもので提案していただければ大丈夫です。

<デザイン>
明るめのやさしい感じでお願いします。
参考サイトほどピンクは強めでなくてもいいかと思いますが、デザイン次第では濃い色の使用もありかと思います。

参考サイト
https://pelrovin.jp/

<ページ幅>
1920pxでお願いします。

<特筆事項>
今回NIVOを使用するにあたりプラン的にNIVOマークが必須になります。
右上のテントのマークはありきでお願いします。

今後も定期的にデザインをお願いすることができる技量を持つ方を探しておりますので是非、単発と考えずにデザインを出していただければと思います。
それでは皆様のご応募よろしくお願い致します。
サイトURL
ページ数
1ページ
希望イメージ
シンプル 複雑
単色 カラフル
暗い 明るい
日常 高級
遊び心 厳粛
未来的 伝統的
女性的 男性的
希望する色
白・淡いピンク・淡い水色などの優しい色
納品ファイル
• フォトショップ形式 (.psd)
補足説明
■ 選んだ理由

こちらが想定した以上のデザインでした。

■ 提案者全員のお礼・コメント

この度は当方コンペにご提案いただきありがとうございました。
提案頂いた方々のデザインはどれも素敵なもので、真剣に吟味し当選者を選択させていただきました。
今後もミルトカを利用してのデザインコンペを行う予定ですので、残念ながら今回は当選とならなかった方もまたご参加いただけると幸いです。
今後もどうかよろしくお願い致します。

```html
<!DOCTYPE html>
<html lang="ja">
<head>
<meta charset="utf-8">
<title>lumetto</title>
<link rel="stylesheet" href="https://fonts.googleapis.com/css2?family=Noto+Sans+JP:wght@400;500;700&family=Noto+Serif+JP:wght@500&family=Poppins:wght@600;700&family=Kalam:wght@700&display=swap">
<style>
  :root {
    --navy: #3b4a6e;
    --ink: #4a4a4a;
    --muted: #7a7a7a;
    --line: #d9d4d4;
    --green: #4f8c4a;
    --taupe: #c6b3ae;
    --taupe-dark: #b9a49f;
    --card-pink: #f6dfe5;
    --card-rose: #ead3da;
    --photo-grey: #8f8e94;
    --btn-a: #f4b6bf;
    --btn-b: #e0848f;
    --hero-bg: #f5f5f6;
  }
  * { margin: 0; padding: 0; box-sizing: border-box; }
  html, body { width: 1200px; height: 2700px; overflow: hidden; background: #fff; }
  body { position: relative; font-family: "Noto Sans JP", sans-serif; color: var(--ink); }

  .site-header { position: absolute; top: 0; left: 0; width: 1200px; height: 88px; display: flex; align-items: center; padding: 0 30px; border-bottom: 1px solid var(--line); }
  .brand { font-family: "Poppins", sans-serif; font-weight: 700; font-size: 46px; color: var(--navy); letter-spacing: 1px; }
  .main-nav { display: flex; margin-left: 70px; }
  .main-nav a { color: var(--muted); text-decoration: none; font-size: 22px; padding: 0 14px; border-left: 2px solid var(--line); }
  .main-nav a:first-child { border-left: none; }
  .header-tools { margin-left: auto; display: flex; gap: 14px; }
  .tool { width: 56px; height: 56px; border: 2px solid var(--navy); display: flex; align-items: center; justify-content: center; font-size: 15px; font-weight: 700; color: var(--navy); }

  .hero { position: absolute; top: 88px; left: 0; width: 1200px; height: 570px; background: linear-gradient(160deg, #fafafa, var(--hero-bg) 60%, #efeff1); border-bottom: 1px solid var(--line); }
  .hero .art { position: absolute; border-radius: 40px; }
  .hero-title { position: absolute; top: 190px; left: 0; width: 1200px; text-align: center; }
  .hero-title .name { font-family: "Poppins", sans-serif; font-weight: 700; font-size: 84px; color: var(--navy); line-height: 1; letter-spacing: 2px; }
  .hero-title .sub { color: var(--green); font-size: 22px; margin-top: 18px; font-weight: 500; }
  .hero-title .pledge { margin-top: 14px; font-size: 20px; color: var(--ink); display: flex; justify-content: center; align-items: center; gap: 8px; }
  .pledge-mark { width: 34px; height: 34px; background: var(--green); border-radius: 4px; }

  .sdgs { position: absolute; top: 700px; left: 0; width: 1200px; height: 200px; }
  .sdgs-badge { position: absolute; left: 130px; top: 20px; width: 150px; height: 150px; border-radius: 50%; background: #8d8d8d; }
  .sdgs-text { position: absolute; left: 320px; top: 28px; width: 820px; font-size: 13px; line-height: 1.85; color: var(--muted); }

  .band { position: absolute; top: 960px; left: 0; }

  .section-title { position: absolute; top: 1150px; width: 1200px; text-align: center; font-family: "Noto Serif JP", serif; font-weight: 500; font-size: 30px; letter-spacing: 3px; color: var(--ink); }

  .card { position: absolute; width: 540px; height: 350px; border: 6px solid var(--navy); background: var(--card-pink); }
  .card.rose { background: var(--card-rose); }
  .card.soft { border-color: #d6c3cb; }
  .card h3 { font-family: "Kalam", cursive; font-weight: 700; font-size: 32px; color: #6a5a55; text-align: center; margin-top: 18px; }
  .card .photo { position: absolute; left: 80px; top: 80px; width: 368px; height: 220px; }
  .c1 { left: 40px; top: 1250px; }
  .c2 { left: 620px; top: 1250px; }
  .c3 { left: 40px; top: 1630px; }
  .c4 { left: 620px; top: 1630px; }

  .btn-list { position: absolute; left: 340px; top: 2060px; width: 520px; height: 90px; border-radius: 45px; background: linear-gradient(90deg, var(--btn-a), var(--btn-b)); display: flex; align-items: center; justify-content: center; color: #fff; font-size: 36px; letter-spacing: 6px; text-decoration: none; }
  .btn-list .arrow { position: absolute; right: 28px; top: 22px; }

  .divider { position: absolute; top: 2210px; left: 0; width: 1200px; border-top: 2px solid var(--line); }

  .info-links { position: absolute; top: 2270px; left: 0; width: 1200px; display: flex; justify-content: space-around; padding: 0 60px; }
  .info-link { width: 220px; text-align: center; color: var(--ink); text-decoration: none; font-size: 22px; }
  .info-link svg { display: block; margin: 0 auto 16px; }

  .site-footer { position: absolute; top: 2540px; left: 0; width: 1200px; height: 160px; background: var(--taupe); color: #fff; text-align: center; padding-top: 42px; }
  .site-footer .legal a { color: #fff; text-decoration: none; font-size: 20px; margin: 0 16px; }
  .site-footer .copy { font-size: 22px; margin-top: 12px; font-weight: 500; }
  .site-footer .copy b { font-family: "Poppins", sans-serif; margin-left: 14px; }
</style>
</head>
<body>

<header class="site-header">
  <div class="brand">lumetto</div>
  <nav class="main-nav">
    <a href="#">会社概要</a><a href="#">商品一覧</a><a href="#">よくある質問</a><a href="#">お問い合わせ</a>
  </nav>
  <div class="header-tools">
    <div class="tool">NIVO</div>
    <div class="tool">
      <svg width="30" height="30" viewBox="0 0 30 30"><path d="M2 4h5l4 15h14l3-10H9" fill="none" stroke="#3b4a6e" stroke-width="2.5"/><circle cx="13" cy="25" r="2.2" fill="#3b4a6e"/><circle cx="23" cy="25" r="2.2" fill="#3b4a6e"/></svg>
    </div>
  </div>
</header>

<section class="hero">
  <div class="art" role="img" aria-label="Pink ballet shoes illustration" style="left:60px;top:70px;width:240px;height:160px;background:linear-gradient(135deg,#f7d9d2,#f0c5bc);"></div>
  <div class="art" role="img" aria-label="Black ankle boots illustration" style="left:110px;top:300px;width:190px;height:230px;background:linear-gradient(135deg,#4b4b4f,#2a2a2c);"></div>
  <div class="art" role="img" aria-label="Pink sneakers illustration" style="left:900px;top:40px;width:190px;height:200px;background:linear-gradient(135deg,#f4c9cd,#e7a8ae);"></div>
  <div class="art" role="img" aria-label="Red high heels illustration" style="left:880px;top:320px;width:270px;height:200px;background:linear-gradient(135deg,#e0454f,#b92632);"></div>
  <div class="hero-title">
    <div class="name">lumetto</div>
    <div class="sub">サステナビリティ</div>
    <div class="pledge">私たちは<span class="pledge-mark"></span>に賛同した企業です</div>
  </div>
</section>

<section class="sdgs">
  <div class="sdgs-badge"></div>
  <p class="sdgs-text">「SDGs（エスディージーズ）」とは、「Sustainable Development Goals（持続可能な開発目標）」の略称です。2015年9月の国連サミットで150を超える加盟国首脳の参加のもと、全会一致で採択された国際目標です。「SDGs（エスディージーズ）」とは、「Sustainable Development Goals（持続可能な開発目標）」の略称です。2015年9月の国連サミットで採択され、誰一人取り残さない社会の実現を目指します。私たちも日々の商品づくりを通して、この目標の達成に取り組んでいます。</p>
</section>

<svg class="band" width="1200" height="140" viewBox="0 0 1200 140">
  <rect x="0" y="0" width="1200" height="50" fill="#c6b3ae"/>
  <polygon points="540,50 660,50 600,120" fill="#c6b3ae"/>
</svg>

<h2 class="section-title">PRODUCT</h2>

<article class="card c1">
  <h3>Ballet Shoes</h3>
  <div class="photo" role="img" aria-label="Ballet shoes product photo" style="background:linear-gradient(135deg,#fff,#fbe9e4);"></div>
</article>
<article class="card rose c2">
  <h3>Room Shoes</h3>
  <div class="photo" role="img" aria-label="Room slippers product photo" style="background:linear-gradient(135deg,#9a99a0,#84838a);"></div>
</article>
<article class="card c3">
  <h3>Disinfectant</h3>
  <div class="photo" role="img" aria-label="Disinfectant spray product photo" style="background:linear-gradient(135deg,#96959b,#85848a);"></div>
</article>
<article class="card soft c4">
  <h3>Mask Case</h3>
  <div class="photo" role="img" aria-label="Mask case product photo" style="background:linear-gradient(135deg,#fff,#f3f3f3);"></div>
</article>

<a class="btn-list" href="#">商品一覧
  <svg class="arrow" width="46" height="46" viewBox="0 0 46 46"><circle cx="23" cy="23" r="22" fill="#fff" opacity=".35"/><polygon points="18,13 33,23 18,33" fill="#fff"/></svg>
</a>

<div class="divider"></div>

<nav class="info-links">
  <a class="info-link" href="#">
    <svg width="90" height="100" viewBox="0 0 90 100" fill="none" stroke="#777" stroke-width="2.5"><rect x="8" y="30" width="36" height="66"/><rect x="44" y="8" width="38" height="88"/><path d="M16 42h8M30 42h8M16 56h8M30 56h8M16 70h8M30 70h8M52 22h8M66 22h8M52 38h8M66 38h8M52 54h8M66 54h8M52 70h8M66 70h8"/></svg>
    会社概要
  </a>
  <a class="info-link" href="#">
    <svg width="100" height="100" viewBox="0 0 100 100" fill="none" stroke="#777" stroke-width="2.5"><rect x="6" y="22" width="70" height="48"/><path d="M6 22l35 28 35-28"/><circle cx="72" cy="72" r="20" fill="#fff"/><path d="M64 64c2-3 5-3 6 0l1 3c0 2-2 3-2 3 2 4 4 6 7 7 0 0 1-2 3-2l3 1c3 1 3 4 0 6-6 3-18-6-18-18z"/></svg>
    お問い合わせ
  </a>
  <a class="info-link" href="#">
    <svg width="100" height="100" viewBox="0 0 100 100"><circle cx="34" cy="32" r="24" fill="#888"/><circle cx="66" cy="66" r="24" fill="#888"/><text x="34" y="41" font-size="26" font-family="Poppins, sans-serif" font-weight="700" fill="#fff" text-anchor="middle">Q</text><text x="66" y="75" font-size="26" font-family="Poppins, sans-serif" font-weight="700" fill="#fff" text-anchor="middle">A</text></svg>
    よくある質問
  </a>
</nav>

<footer class="site-footer">
  <div class="legal"><a href="#">特定商取引に基づく表記</a><a href="#">プライバシーポリシー</a></div>
  <div class="copy">@2020<b>lumetto</b></div>
</footer>

</body>
</html>
```